New hardcover book cover

I want a striking, eye-catching cover with title, subtitle and a picture.See for previous book covers: www.brightmaplepress.com

Target Market(s)

young, successful entrepreneurs that have built a business in a niche market that they discovered.

Font styles to use
Serif

Colors

Designer to choose colors to be used in the design.

Requirements
Must have
• A book cover that impresses and captures the imagination of those who look at it.
• MY MISTAKE, SORRY.
• Title: Founders Behind the Quiet Trade Boom
• Subtitle: 25 stories of success from
• discovering hidden opportunities
• Author: Dorian Pelham
• Please use the photo attached, thanks.

```html
<!DOCTYPE html>
<html lang="en">
<head>
<meta charset="utf-8">
<title>Founders Behind the Quiet Trade Boom — Dorian Pelham</title>
<link rel="stylesheet" href="https://fonts.googleapis.com/css2?family=Oswald:wght@600&family=Chivo:wght@400&display=swap">
<style>
  :root {
    --backdrop: #e2dfd8;
    --band-red: #9a0f30;
    --title-red: #a3122f;
    --title-navy: #12336a;
    --sky-light: #ecebe6;
    --sky-blue: #b9d3ea;
    --ring-grey: #8e97ab;
    --ring-dark: #2f3250;
    --target-red: #a51c3c;
    --white: #ffffff;
  }
  html, body {
    margin: 0;
    width: 1200px;
    height: 1200px;
    overflow: hidden;
    background: var(--backdrop);
  }
  .cover {
    position: absolute;
    left: 215px;
    top: 40px;
    width: 770px;
    height: 1120px;
    overflow: hidden;
    background: var(--sky-light);
  }
  .author-band {
    position: absolute;
    left: 0; top: 0;
    width: 100%;
    height: 100px;
    background: var(--band-red);
    display: flex;
    align-items: center;
    justify-content: center;
  }
  .author-name {
    margin: 0;
    font-family: "Chivo", sans-serif;
    font-weight: 400;
    font-size: 30px;
    letter-spacing: 0.36em;
    color: var(--white);
    text-transform: uppercase;
    padding-left: 0.36em;
  }
  .cover-art {
    position: absolute;
    left: 0; top: 100px;
    width: 770px;
    height: 1020px;
  }
  .title {
    position: absolute;
    left: 76px;
    right: 90px;
    top: 130px;
    margin: 0;
    font-family: "Oswald", sans-serif;
    font-weight: 600;
    text-transform: uppercase;
    line-height: 0.98;
  }
  .title-line { display: flex; align-items: center; white-space: nowrap; }
  .title-lead { font-size: 96px; color: var(--title-red); letter-spacing: -0.01em; }
  .title-main { font-size: 96px; color: var(--title-navy); letter-spacing: -0.01em; }
  .title-joiner {
    display: flex;
    flex-direction: column;
    font-size: 34px;
    line-height: 0.95;
    color: var(--title-red);
    margin-right: 10px;
    text-align: center;
  }
  .subtitle {
    position: absolute;
    left: 0;
    width: 100%;
    top: 960px;
    margin: 0;
    text-align: center;
    font-family: "Chivo", sans-serif;
    font-weight: 400;
    font-size: 28px;
    line-height: 1.3;
    color: var(--white);
  }
</style>
</head>
<body>
  <article class="cover">
    <svg class="cover-art" viewBox="0 0 770 1020" role="img" aria-label="Photograph of an arrow striking the red centre of an archery target under a bright sky">
      <defs>
        <linearGradient id="sky" x1="0" y1="0" x2="0.3" y2="1">
          <stop offset="0" stop-color="var(--sky-light)"/>
          <stop offset="0.3" stop-color="var(--sky-blue)"/>
          <stop offset="0.45" stop-color="var(--ring-grey)"/>
          <stop offset="0.65" stop-color="var(--ring-dark)"/>
          <stop offset="1" stop-color="var(--target-red)"/>
        </linearGradient>
        <radialGradient id="bullseye" cx="0.52" cy="0.78" r="0.35">
          <stop offset="0" stop-color="var(--target-red)" stop-opacity="0.9"/>
          <stop offset="1" stop-color="var(--target-red)" stop-opacity="0"/>
        </radialGradient>
      </defs>
      <rect width="770" height="1020" fill="url(#sky)"/>
      <rect width="770" height="1020" fill="url(#bullseye)"/>
    </svg>

    <header class="author-band">
      <p class="author-name">Dorian Pelham</p>
    </header>

    <h1 class="title">
      <span class="title-line title-lead">Founders</span>
      <span class="title-line">
        <span class="title-joiner"><span>Behind</span><span>the</span></span>
        <span class="title-main">Quiet Trade</span>
      </span>
      <span class="title-line title-main">Boom</span>
    </h1>

    <p class="subtitle">25 stories of success from<br>discovering hidden opportunities</p>
  </article>
</body>
</html>
```